Health care technology software systems

We have a solid logo. We have company colors that will need to be used as well. We just need a great business card design. We sell to health plans but want to be modern
Updates

Need extra days to review

Target Market(s)

Health technology sector selling into Health Plans

Industry/Entity Type

Health Care Technology

Contact Information for Business Card

Name, title, address, phone number, email

Requirements
Must have
• Use of Kembrata corporate colors - Uploaded w/ our logos

```html
<!DOCTYPE html>
<html lang="en">
<head>
<meta charset="UTF-8">
<title>Kembrata Business Card</title>
<link href="https://fonts.googleapis.com/css2?family=Roboto:wght@300;400;500&display=swap" rel="stylesheet">
<style>
  :root {
    --page-bg: #eeeeee;
    --card-white: #ffffff;
    --card-dark: #3d4443;
    --brand-blue: #0669ad;
    --brand-cyan: #0ea5dc;
    --ink: #3d4443;
    --ink-soft: #444a49;
    --on-dark: #ffffff;
  }
  * { margin: 0; padding: 0; box-sizing: border-box; }
  html, body {
    width: 1200px; height: 1200px; overflow: hidden;
    background: var(--page-bg);
    font-family: "Roboto", Arial, sans-serif;
  }
  .canvas { position: relative; width: 1200px; height: 1200px; }
  .card {
    position: absolute; left: 281px; width: 639px; height: 365px;
    border-radius: 22px; overflow: hidden;
    box-shadow: 6px 8px 10px rgba(0,0,0,0.28);
  }
  .card--front { top: 191px; background: var(--card-white); }
  .card--back { top: 643px; background: var(--card-dark); }

  .brand { position: absolute; display: flex; align-items: center; gap: 34px; }
  .brand__dot { width: 76px; height: 76px; border-radius: 50%; background: var(--brand-blue); }
  .brand__name {
    font-family: "Roboto", Arial, sans-serif; font-weight: 300;
    font-size: 86px; line-height: 1; letter-spacing: 1px; color: var(--ink);
  }
  .card--front .brand { left: 114px; top: 51px; }
  .card--back .brand { left: 114px; top: 144px; }
  .card--back .brand__dot { background: var(--brand-cyan); }
  .card--back .brand__name { color: var(--on-dark); }

  .person { position: absolute; left: 73px; top: 212px; }
  .person__name { font-size: 25px; font-weight: 500; color: var(--brand-blue); line-height: 30px; }
  .person__title { font-size: 20px; font-weight: 400; color: var(--ink-soft); line-height: 26px; }

  .divider { position: absolute; left: 318px; top: 177px; width: 2px; height: 123px; background: var(--brand-blue); }

  .contact { position: absolute; left: 350px; top: 182px; font-size: 17px; color: var(--ink-soft); line-height: 20px; }
  .contact__address { margin-bottom: 20px; }
  .contact__row { display: flex; align-items: center; gap: 6px; margin-bottom: 9px; }
  .contact__icon { width: 14px; height: 14px; flex: none; }

  .web-band {
    position: absolute; left: 0; bottom: 0; width: 100%; height: 41px;
    background: var(--brand-blue); color: var(--on-dark);
    font-size: 17px; text-align: center; line-height: 44px;
  }
</style>
</head>
<body>
<div class="canvas">
  <section class="card card--front">
    <div class="brand">
      <span class="brand__dot"></span>
      <span class="brand__name">kembrata</span>
    </div>

    <div class="person">
      <p class="person__name">LOREM LPSUM</p>
      <p class="person__title">Founder</p>
    </div>

    <div class="divider"></div>

    <div class="contact">
      <p class="contact__address">123, Dummy Road, Lorem ipsum,<br>County, DR 12345</p>
      <p class="contact__row">
        <svg class="contact__icon" viewBox="0 0 24 24" aria-hidden="true"><path fill="#0669ad" d="M6.6 10.8c1.4 2.8 3.8 5.1 6.6 6.6l2.2-2.2c.3-.3.7-.4 1-.2 1.1.4 2.3.6 3.6.6.6 0 1 .4 1 1V20c0 .6-.4 1-1 1C10.6 21 3 13.4 3 4c0-.6.4-1 1-1h3.5c.6 0 1 .4 1 1 0 1.3.2 2.5.6 3.6.1.3 0 .7-.2 1L6.6 10.8z"/></svg>
        (000) 123-4567
      </p>
      <p class="contact__row">
        <svg class="contact__icon" viewBox="0 0 24 24" aria-hidden="true"><rect x="2" y="5" width="20" height="14" fill="#0669ad"/><path d="M2 5l10 8 10-8" fill="none" stroke="#ffffff" stroke-width="1.6"/></svg>
        info@kembrata.com
      </p>
    </div>

    <div class="web-band">www.kembrata.com</div>
  </section>

  <section class="card card--back">
    <div class="brand">
      <span class="brand__dot"></span>
      <span class="brand__name">kembrata</span>
    </div>
  </section>
</div>
</body>
</html>
```